Pale Fern The Vapor Parlor needs a room spray label

We are a company that is dedicated to the aromatization services for our customers, we have just created an aromatic product that is a Room Spray for the customer to spray it in their spaces and we are looking for the most sophisticated and luxurious label in the market, help us? Thanks a lot!

Target Market(s)

That the label represents an elegant and exclusive aroma

Font styles to use
Serif

Colors

Designer to choose colors to be used in the design.

Requirements
Must have
• Elegance, fine, luxury and cleanliness
Nice to have
• The fonts I like are those of the logo, they are called "Cinzel_Regular" and "MrEaveXL"
They can propose in color but I think it looks better in black and gray or white, however I would like to see something in color

```html
<!DOCTYPE html>
<html lang="es">
<head>
<meta charset="utf-8">
<title>Pale Fern The Vapor Parlor – Room Spray Label</title>
<link rel="stylesheet" href="https://fonts.googleapis.com/css2?family=Cinzel:wght@400;700&display=swap">
<style>
  :root {
    --backdrop: #5a70b8;
    --backdrop-deep: #4456a3;
    --label-white: #f6f6f6;
    --label-shade: #e9e9e9;
    --gold: #c9a02e;
    --gold-light: #e0c766;
    --gold-deep: #d4a348;
    --ink: #1d1d1d;
    --ink-soft: #2b2b2b;
  }
  * { margin: 0; padding: 0; box-sizing: border-box; }
  html, body {
    width: 950px;
    height: 1200px;
    overflow: hidden;
  }
  body {
    background: radial-gradient(circle at 35% 40%, var(--backdrop) 0%, var(--backdrop-deep) 80%);
    font-family: "Cinzel", serif;
  }
  .label {
    position: absolute;
    left: 302px;
    top: 30px;
    width: 345px;
    height: 1138px;
    background: linear-gradient(90deg, var(--label-shade) 0%, var(--label-white) 30%, var(--label-white) 70%, var(--label-shade) 100%);
    border-radius: 6px;
  }
  .band {
    position: absolute;
    left: 0;
    width: 100%;
    background: linear-gradient(90deg, var(--gold-deep) 0%, var(--gold-light) 50%, var(--gold-deep) 100%);
  }
  .band--top { top: 50px; height: 44px; }
  .band--rule { top: 1000px; height: 4px; }
  .band--bottom {
    top: 1015px;
    height: 77px;
    display: flex;
    align-items: center;
    justify-content: center;
  }
  .brand-mark {
    position: absolute;
    left: 112px;
    top: 194px;
    width: 120px;
    height: 120px;
    border-radius: 50%;
    background: var(--gold);
  }
  .brand-name,
  .brand-tagline {
    position: absolute;
    left: 0;
    width: 100%;
    text-align: center;
    color: var(--gold);
    font-weight: 400;
    white-space: nowrap;
  }
  .brand-name {
    top: 412px;
    font-size: 38px;
    line-height: 50px;
  }
  .brand-tagline {
    top: 462px;
    font-size: 14px;
    line-height: 20px;
    letter-spacing: 0.3em;
  }
  .rule {
    position: absolute;
    height: 2px;
    background: var(--gold);
  }
  .rule--upper { left: 34px; width: 273px; top: 560px; }
  .rule--lower { left: 67px; width: 206px; top: 642px; }
  .ornament {
    position: absolute;
    background: radial-gradient(ellipse at center, rgba(201,160,46,0.45) 0%, rgba(201,160,46,0.12) 60%, rgba(201,160,46,0) 75%);
  }
  .ornament--upper { left: 101px; top: 508px; width: 134px; height: 52px; }
  .ornament--lower { left: 122px; top: 645px; width: 96px; height: 36px; }
  .product-name {
    position: absolute;
    left: 0;
    top: 576px;
    width: 100%;
    text-align: center;
    font-size: 46px;
    line-height: 54px;
    letter-spacing: 0.08em;
    color: var(--ink);
  }
  .spec {
    position: absolute;
    left: 0;
    width: 100%;
    text-align: center;
    white-space: nowrap;
  }
  .spec--percent {
    top: 742px;
    font-size: 34px;
    line-height: 42px;
    font-weight: 700;
    color: var(--gold);
  }
  .spec--blend {
    top: 791px;
    font-size: 18px;
    line-height: 24px;
    color: var(--ink-soft);
  }
  .spec--aromatic {
    top: 826px;
    font-size: 28px;
    line-height: 34px;
    color: var(--ink-soft);
  }
  .spec--net {
    top: 868px;
    font-size: 18px;
    line-height: 24px;
    color: var(--ink-soft);
  }
  .volume {
    font-size: 28px;
    letter-spacing: 0.04em;
    color: var(--ink);
  }
</style>
</head>
<body>
  <main class="label">
    <div class="band band--top"></div>

    <div class="brand-mark"></div>
    <p class="brand-name">PALE FERN</p>
    <p class="brand-tagline">THE VAPOR PARLOR</p>

    <div class="ornament ornament--upper" role="img" aria-label="Gold leaf ornament above the product name"></div>
    <div class="rule rule--upper"></div>
    <h1 class="product-name">DAPPER</h1>
    <div class="rule rule--lower"></div>
    <div class="ornament ornament--lower" role="img" aria-label="Gold leaf ornament below the product name"></div>

    <p class="spec spec--percent">100%</p>
    <p class="spec spec--blend">MEZCLA DE ACEITES</p>
    <p class="spec spec--aromatic">AROMATICOS</p>
    <p class="spec spec--net">CONTENIDO NETO</p>

    <div class="band band--rule"></div>
    <div class="band band--bottom"><span class="volume">60ML</span></div>
  </main>
</body>
</html>
```